Delvin & Associates - London New Letting and Property Management Company *

Delvin & Associates LTD is a new company based in London, and works with brand new residential property in the city centre.

We are aiming to have 1000 new properties a year.

We are looking for something modern and minimalistic :
Logo ,Monogram, Paper Head and Business Card.

Target Market(s)

Internation landlords

Industry/Entity Type

Real Estate

Logo Text

Delvin & Associates

Colors

Designer to choose colors to be used in the design.

Requirements
Nice to have
• A particular monogram with "DA"
Should not have
• Little House over the logo

```html
<!DOCTYPE html>
<html lang="en">
<head>
<meta charset="utf-8">
<title>Delvin &amp; Associates – Business Card</title>
<link rel="stylesheet" href="https://fonts.googleapis.com/css2?family=Raleway:wght@400;500&display=swap">
<style>
  :root {
    --card: #f39c77;
    --ink: #ffffff;
    --page: #ffffff;
    --label: #333333;
    --shadow: rgba(40, 40, 40, 0.55);
  }
  * { box-sizing: border-box; margin: 0; padding: 0; }
  html, body {
    width: 1200px; height: 1200px; overflow: hidden;
    background: var(--page);
    font-family: "Raleway", Arial, sans-serif;
  }
  .sheet { position: relative; width: 1200px; height: 1200px; }

  .side-label {
    position: absolute;
    transform: rotate(-90deg);
    transform-origin: left top;
    font-size: 9px; letter-spacing: 0.02em;
    color: var(--label);
    white-space: nowrap;
    display: flex; align-items: center; gap: 6px;
  }
  .side-label::before {
    content: ""; width: 10px; height: 6px; background: var(--card);
  }
  .side-label--back  { left: 58px;  top: 478px; }
  .side-label--front { left: 336px; top: 1144px; }

  .card {
    position: absolute;
    width: 702px; height: 401px;
    background: var(--card);
    color: var(--ink);
    box-shadow: 14px 14px 12px var(--shadow);
    overflow: hidden;
  }
  .card--back  { left: 120px; top: 72px; }
  .card--front { left: 393px; top: 742px; }

  .brand {
    position: absolute;
    display: flex; align-items: center; gap: 14px;
    font-weight: 500; color: var(--ink);
    white-space: nowrap;
  }
  .brand__dot { border-radius: 50%; background: var(--ink); flex: none; }
  .card--back .brand { left: 218px; top: 176px; font-size: 27px; }
  .card--back .brand__dot { width: 34px; height: 34px; }
  .card--front .brand { left: 35px; top: 52px; font-size: 19px; gap: 10px; }
  .card--front .brand__dot { width: 24px; height: 24px; }

  .rule { position: absolute; background: var(--ink); }
  .rule--v1 { left: 247px; top: 0; width: 2px; height: 100%; }
  .rule--v2 { left: 357px; top: 0; width: 2px; height: 100%; }
  .rule--h  { left: 0; top: 280px; width: 100%; height: 2px; }

  .person { position: absolute; left: 375px; top: 211px; }
  .person__name { font-size: 23px; font-weight: 500; letter-spacing: 0.04em; line-height: 1; }
  .person__role { font-size: 18px; font-weight: 400; margin-top: 11px; letter-spacing: 0.02em; line-height: 1; }

  .contact { position: absolute; left: 375px; top: 298px; list-style: none; }
  .contact li { font-size: 15px; letter-spacing: 0.06em; height: 33.5px; line-height: 1; }

  .website {
    position: absolute; left: 35px; top: 365px;
    font-size: 15.5px; letter-spacing: 0.06em; line-height: 1;
  }
</style>
</head>
<body>
<main class="sheet">
  <span class="side-label side-label--back">BUSINESS CARD BACK</span>
  <section class="card card--back" aria-label="Business card back">
    <div class="brand"><span class="brand__dot"></span>Delvin &amp; Associates</div>
  </section>

  <span class="side-label side-label--front">BUSINESS CARD FRONT</span>
  <section class="card card--front" aria-label="Business card front">
    <div class="brand"><span class="brand__dot"></span>Delvin &amp; Associates</div>
    <span class="rule rule--v1"></span>
    <span class="rule rule--v2"></span>
    <span class="rule rule--h"></span>
    <div class="person">
      <p class="person__name">TOM HARLOW</p>
      <p class="person__role">Director</p>
    </div>
    <ul class="contact">
      <li>+44 (0) 20 7946 0321</li>
      <li>tharlow@delvinassoc.co.uk</li>
      <li>12 Elmfield Row, London.</li>
    </ul>
    <p class="website">delvinassoc.co.uk</p>
  </section>
</main>
</body>
</html>
```